Seafood Restaurant Outdoor Menu Board

Corvell's Seafood, a legendary local seafood restaurant in Ventura, CA USA, most widely known for its fish and chips and clam chowder, needs refreshed outdoor menu boards!

You can see the existing menu board at https://www.pictoshare.example/p/K8mR2Wxq51T/

and get inspiration from our website, https://corvellsseafood.example

Please use your design for 2 sets of menu items, to be displayed side by side as in the photo:
Menu Board #1: "Customer Favorites"
- Grilled Halibut
- Grilled Salmon Filet
- Grilled Shrimp Skewers
- Corvell's Fish & Chips
- 14pc Shrimp & Chips
- Harbor Trio
- Onion Rings
- Clam Chowder Lantern
- Large Clam Chowder
- Small Clam Chowder
Menu Board #2: "Grilled Dinners"
GR HALIBUT $21.80
BAKED HALIBUT $26.95
GR SNAPPER $21.95
GR AHI $25.85
GR SALMON FILLET $20.90
GR YELLOWTAIL $12.65
GR BLACK SEA BASS $20.99
GR SHRIMP SKEWERS $23.10
GR WHITE SEA BASS $21.60
GR SWORDFISH $27.75
GR MAHI $7.95
GR COD $10.40

SERVED WITH RICE PILAF & BREAD & YOUR CHOICE OF PASTA SALAD, COLE SLAW, OR GREEN SALAD

Our landlord has provided the following guidelines for the new menu board:
- Public Facing Exterior Menu boards need overall simplification and reduction of the information offered while still highlighting major sellers and up sellers.
- Need to be designed as elegant wall signs rather than a list of menu items. (see examples)
- Less is More.
- Easy to read and understand, equally spaced information, good use of negative space.
- Draw customers eyes to the most desirable products.
- Layout: The layout should be professionally done, with sufficient negative space around menu items.
- Fonts: 3 Fonts maximum, encouraging sans serif font styles for easy readability.
- Established 1982: Arial Rounded MT Bold
- Menu Boards: Myriad Pro - Bold Condensed
- Smaller Directional Signs: Arial
- Colors: Tied to organization branding, 3 colors maximum. Please use a light-colored background. Our brand colors are:
- Primary: #233F94
- Secondary: #0F65A7
- Tertiary: 32A0CA
- Contrast: #F7F4DB
Attention: #ED4224
Icons: Use of simplified icons are allowed and encouraged to highlight and organize menu sections

```html
<!DOCTYPE html>
<html lang="en">
<head>
<meta charset="utf-8">
<title>Corvell's Seafood – Outdoor Menu Boards</title>
<link rel="stylesheet" href="https://fonts.googleapis.com/css2?family=Montserrat:wght@600&family=Poppins:wght@600;700;800&family=Kaushan+Script&display=swap">
<style>
  :root {
    --stage: #a4a7b4;
    --paper: #eeeff1;
    --navy: #101f86;
    --navy-deep: #0b1766;
    --pill-navy: #24409a;
    --sky: #2f9fcf;
    --yellow: #ffe31c;
    --white: #ffffff;
    --ink: #1a1f3a;
    --photo-warm: #d39b52;
    --photo-cool: #c9ced8;
  }
  * { box-sizing: border-box; margin: 0; padding: 0; }
  html, body { width: 1200px; height: 3050px; overflow: hidden; }
  body { background: var(--stage); position: relative; font-family: "Poppins", sans-serif; }

  .board {
    position: absolute; left: 198px; width: 782px; height: 1302px;
    background: radial-gradient(ellipse at 40% 60%, #f6f6f8 0%, var(--paper) 60%, #e4e5e9 100%);
    overflow: hidden;
  }
  .board--favorites { top: 148px; }
  .board--grilled { top: 1575px; }
  .board > * { position: absolute; }

  .band { left: 0; top: 0; width: 782px; height: 1302px; }

  .sketch { border-radius: 50%; background: rgba(30, 50, 90, 0.07); }
  .sketch--on-band { background: rgba(47, 159, 207, 0.18); }

  .brand-name {
    font-family: "Poppins", sans-serif; font-weight: 800; color: var(--navy);
    text-align: center; line-height: 1.05;
  }

  .title-seafood {
    font-family: "Montserrat", sans-serif; font-weight: 600; color: var(--sky);
    font-size: 112px; line-height: 1; letter-spacing: -2px;
  }
  .title-menu {
    font-family: "Kaushan Script", cursive; color: var(--yellow);
    font-size: 150px; line-height: 1; transform: rotate(-6deg);
  }
  .section-title {
    font-family: "Poppins", sans-serif; font-weight: 800; color: var(--white);
    line-height: 1;
  }

  .photo { background: linear-gradient(135deg, #e9c48a, var(--photo-warm) 55%, #a9703a); border-radius: 18px; opacity: 0.95; }

  /* favourites list */
  .fav-list { list-style: none; left: 0; top: 0; }
  .fav-item {
    position: absolute; width: 347px; height: 53px;
    display: flex; align-items: center; gap: 12px; padding-left: 22px;
    color: var(--white); font-weight: 600; font-size: 24px; white-space: nowrap;
  }
  .fav-item::before {
    content: ""; position: absolute; inset: 0; z-index: 0;
    transform: skewX(-12deg); background: var(--sky);
  }
  .fav-item--dark::before { background: var(--pill-navy); }
  .fav-item > * { position: relative; z-index: 1; }
  .tick { width: 20px; height: 20px; flex: none; }

  /* grilled list */
  .price-row { position: absolute; display: flex; height: 45px; font-weight: 700; font-size: 21px; }
  .price-row__name, .price-row__price {
    position: relative; display: flex; align-items: center; height: 100%;
  }
  .price-row__name { width: 248px; padding-left: 20px; color: var(--white); }
  .price-row__price { width: 98px; padding-left: 12px; color: var(--yellow); }
  .price-row__name::before, .price-row__price::before {
    content: ""; position: absolute; inset: 0; transform: skewX(-12deg); z-index: 0;
  }
  .price-row__name::before { background: var(--sky); }
  .price-row__price::before { background: var(--navy-deep); left: 4px; }
  .price-row span { position: relative; z-index: 1; }

  .serving-note {
    font-weight: 700; font-size: 17.5px; line-height: 1.3; color: var(--ink);
  }
</style>
</head>
<body>

<!-- Board 1: Customer Favorites -->
<section class="board board--favorites" aria-label="Customer favorites menu board">
  <div class="sketch" role="img" aria-label="Line sketch of a lemon slice" style="left:170px;top:0;width:70px;height:50px"></div>
  <div class="sketch" role="img" aria-label="Line sketch of a shrimp" style="left:0;top:110px;width:130px;height:100px"></div>
  <div class="sketch" role="img" aria-label="Line sketch of a crab" style="left:570px;top:0;width:180px;height:110px"></div>

  <svg class="band" viewBox="0 0 782 1302" aria-hidden="true">
    <defs>
      <linearGradient id="bandFav" x1="0" y1="0" x2="0" y2="1">
        <stop offset="0" stop-color="#0d1d7c"/><stop offset="1" stop-color="#122593"/>
      </linearGradient>
    </defs>
    <polygon fill="url(#bandFav)" points="0,252 40,246 62,249 95,238 140,242 182,234 230,230 262,224 300,229 345,218 392,216 420,212 470,210 505,203 545,205 580,198 620,199 662,193 700,195 740,186 782,184 782,556 748,560 720,568 690,566 650,574 612,571 570,580 540,578 500,586 462,588 430,596 392,594 350,604 318,602 280,612 240,616 210,622 170,626 135,634 98,636 62,646 30,644 0,656"/>
  </svg>
  <div class="sketch sketch--on-band" role="img" aria-label="Line sketch of a lemon slice" style="left:720px;top:205px;width:62px;height:90px"></div>
  <div class="sketch sketch--on-band" role="img" aria-label="Line sketch of a crab" style="left:0;top:375px;width:80px;height:100px"></div>

  <p class="brand-name" style="left:190px;top:70px;width:400px;font-size:48px">Corvell's Seafood</p>

  <h1 class="title-seafood" style="left:133px;top:262px">SEAFOOD</h1>
  <p class="title-menu" style="left:215px;top:315px">Menu</p>
  <h2 class="section-title" style="left:60px;top:490px;font-size:55px;letter-spacing:3px">CUSTOMER FAVORITES</h2>

  <div class="photo" role="img" aria-label="Photo of fried fish and chips in a wire basket with cocktail sauce" style="left:417px;top:620px;width:365px;height:180px"></div>

  <ul class="fav-list">
    <li class="fav-item" style="left:45px;top:702px"><svg class="tick" viewBox="0 0 20 20"><circle cx="10" cy="10" r="10" fill="#0b1766"/><path d="M5.5 10.2l3 3 6-6" stroke="#fff" stroke-width="2.4" fill="none" stroke-linecap="round"/></svg><span>Grilled Halibut</span></li>
    <li class="fav-item" style="left:45px;top:779px"><svg class="tick" viewBox="0 0 20 20"><circle cx="10" cy="10" r="10" fill="#0b1766"/><path d="M5.5 10.2l3 3 6-6" stroke="#fff" stroke-width="2.4" fill="none" stroke-linecap="round"/></svg><span>Grilled Salmon Filet</span></li>
    <li class="fav-item" style="left:45px;top:854px"><svg class="tick" viewBox="0 0 20 20"><circle cx="10" cy="10" r="10" fill="#0b1766"/><path d="M5.5 10.2l3 3 6-6" stroke="#fff" stroke-width="2.4" fill="none" stroke-linecap="round"/></svg><span>Grilled Shrimp Skewers</span></li>
    <li class="fav-item" style="left:45px;top:927px"><svg class="tick" viewBox="0 0 20 20"><circle cx="10" cy="10" r="10" fill="#0b1766"/><path d="M5.5 10.2l3 3 6-6" stroke="#fff" stroke-width="2.4" fill="none" stroke-linecap="round"/></svg><span>Corvell's Fish &amp; Chips</span></li>
    <li class="fav-item" style="left:45px;top:1003px"><svg class="tick" viewBox="0 0 20 20"><circle cx="10" cy="10" r="10" fill="#0b1766"/><path d="M5.5 10.2l3 3 6-6" stroke="#fff" stroke-width="2.4" fill="none" stroke-linecap="round"/></svg><span>14pc Shrimp &amp; Chips</span></li>

    <li class="fav-item fav-item--dark" style="left:402px;top:854px"><svg class="tick" viewBox="0 0 20 20"><circle cx="10" cy="10" r="10" fill="#2f9fcf"/><path d="M5.5 10.2l3 3 6-6" stroke="#fff" stroke-width="2.4" fill="none" stroke-linecap="round"/></svg><span>Harbor Trio</span></li>
    <li class="fav-item fav-item--dark" style="left:402px;top:927px"><svg class="tick" viewBox="0 0 20 20"><circle cx="10" cy="10" r="10" fill="#2f9fcf"/><path d="M5.5 10.2l3 3 6-6" stroke="#fff" stroke-width="2.4" fill="none" stroke-linecap="round"/></svg><span>Onion Rings</span></li>
    <li class="fav-item fav-item--dark" style="left:402px;top:1003px"><svg class="tick" viewBox="0 0 20 20"><circle cx="10" cy="10" r="10" fill="#2f9fcf"/><path d="M5.5 10.2l3 3 6-6" stroke="#fff" stroke-width="2.4" fill="none" stroke-linecap="round"/></svg><span>Clam Chowder Lantern</span></li>
    <li class="fav-item fav-item--dark" style="left:402px;top:1079px"><svg class="tick" viewBox="0 0 20 20"><circle cx="10" cy="10" r="10" fill="#2f9fcf"/><path d="M5.5 10.2l3 3 6-6" stroke="#fff" stroke-width="2.4" fill="none" stroke-linecap="round"/></svg><span>Large Clam Chowder</span></li>
    <li class="fav-item fav-item--dark" style="left:402px;top:1155px"><svg class="tick" viewBox="0 0 20 20"><circle cx="10" cy="10" r="10" fill="#2f9fcf"/><path d="M5.5 10.2l3 3 6-6" stroke="#fff" stroke-width="2.4" fill="none" stroke-linecap="round"/></svg><span>Small Clam Chowder</span></li>
  </ul>

  <div class="photo" role="img" aria-label="Photo of grilled shrimp skewers with pasta salad, rice and a bread roll on a plate" style="left:0;top:1060px;width:388px;height:212px;background:linear-gradient(120deg,#e0c08a,#c98a4c 50%,#7f9a58)"></div>
  <div class="sketch" role="img" aria-label="Line sketch of a lemon slice" style="left:730px;top:1250px;width:60px;height:60px"></div>
</section>

<!-- Board 2: Grilled Dinners -->
<section class="board board--grilled" aria-label="Grilled dinners menu board">
  <svg class="band" viewBox="0 0 782 1302" aria-hidden="true">
    <defs>
      <linearGradient id="bandGrill" x1="0" y1="0" x2="0" y2="1">
        <stop offset="0" stop-color="#0d1d7c"/><stop offset="1" stop-color="#122593"/>
      </linearGradient>
    </defs>
    <polygon fill="url(#bandGrill)" points="0,0 782,0 782,440 700,444 620,446 560,450 520,452 490,446 460,448 430,454 395,450 360,456 320,452 285,458 250,455 215,462 180,459 140,462 110,470 80,466 50,472 25,468 0,474"/>
  </svg>
  <div class="sketch sketch--on-band" role="img" aria-label="Line sketch of a lemon slice" style="left:160px;top:0;width:75px;height:45px"></div>
  <div class="sketch sketch--on-band" role="img" aria-label="Line sketch of a herb sprig" style="left:730px;top:0;width:52px;height:45px"></div>
  <div class="sketch sketch--on-band" role="img" aria-label="Line sketch of a lemon slice" style="left:728px;top:210px;width:54px;height:80px"></div>
  <div class="sketch sketch--on-band" role="img" aria-label="Line sketch of a crab" style="left:0;top:355px;width:60px;height:110px"></div>

  <h1 class="title-seafood" style="left:57px;top:68px">SEAFOOD</h1>
  <p class="title-menu" style="left:78px;top:115px">Menu</p>
  <h2 class="section-title" style="left:60px;top:290px;font-size:53px;letter-spacing:3px;line-height:1">GRILLED<br>DINNERS</h2>

  <div class="photo" role="img" aria-label="Photo of fried fish and potato wedges with a lemon wedge on a black plate" style="left:400px;top:188px;width:400px;height:398px;border-radius:50%;background:radial-gradient(circle,#d7964a 0%,#c27a35 48%,#1d1d1f 62%,#111 100%)"></div>

  <div class="price-row" style="left:39px;top:509px"><div class="price-row__name"><span>GR HALIBUT</span></div><div class="price-row__price"><span>$21.80</span></div></div>
  <div class="price-row" style="left:39px;top:574px"><div class="price-row__name"><span>BAKED HALIBUT</span></div><div class="price-row__price"><span>$26.95</span></div></div>
  <div class="price-row" style="left:39px;top:639px"><div class="price-row__name"><span>GR SNAPPER</span></div><div class="price-row__price"><span>$21.95</span></div></div>
  <div class="price-row" style="left:39px;top:704px"><div class="price-row__name"><span>GR AHI</span></div><div class="price-row__price"><span>$25.85</span></div></div>
  <div class="price-row" style="left:39px;top:769px"><div class="price-row__name"><span>GR SALMON FILLET</span></div><div class="price-row__price"><span>$20.90</span></div></div>
  <div class="price-row" style="left:39px;top:834px"><div class="price-row__name"><span>GR YELLOWTAIL</span></div><div class="price-row__price"><span>$12.65</span></div></div>

  <div class="price-row" style="left:391px;top:636px"><div class="price-row__name" style="padding-left:12px"><span>GR BLACK SEA BASS</span></div><div class="price-row__price"><span>$20.99</span></div></div>
  <div class="price-row" style="left:391px;top:701px"><div class="price-row__name" style="padding-left:12px"><span>GR SHRIMP SKEWERS</span></div><div class="price-row__price"><span>$23.10</span></div></div>
  <div class="price-row" style="left:391px;top:766px"><div class="price-row__name" style="padding-left:12px"><span>GR WHITE SEA BASS</span></div><div class="price-row__price"><span>$21.60</span></div></div>
  <div class="price-row" style="left:391px;top:831px"><div class="price-row__name" style="padding-left:12px"><span>GR SWORDFISH</span></div><div class="price-row__price"><span>$27.75</span></div></div>
  <div class="price-row" style="left:391px;top:896px"><div class="price-row__name" style="padding-left:12px"><span>GR MAHI</span></div><div class="price-row__price"><span>$7.95</span></div></div>
  <div class="price-row" style="left:391px;top:961px"><div class="price-row__name" style="padding-left:12px"><span>GR COD</span></div><div class="price-row__price"><span>$10.40</span></div></div>

  <p class="brand-name" style="left:40px;top:950px;width:280px;font-size:44px">Corvell's Seafood</p>

  <p class="serving-note" style="left:391px;top:1046px;width:370px">SERVED WITH RICE PILAF &amp; BREAD &amp; YOUR CHOICE OF PASTA SALAD, COLE SLAW, OR GREEN SALAD</p>

  <div class="photo" role="img" aria-label="Photo of fresh seafood: mussels, whole fish, scallop shells and octopus" style="left:0;top:1122px;width:782px;height:180px;border-radius:0;background:linear-gradient(180deg,rgba(238,239,241,0) 0%,#b8a9a8 35%,#6f6a72 70%,#3e3a44 100%)"></div>
</section>

</body>
</html>
```